LumaLearn.net the Free Online Tutorial Needs a New Web Design

We need a new web design for our existing website, LumaLearn.net. We provide a Free Online Tutorial of any code, like HTML, CSS, PHP, Jquery, javascript etc, including online editor.
We would like to see designs that interesting, simple, interactive, and be a very comfortable place to read in a long time.
We need 2 pages design for:
1. Home Page (http://lumalearn.net) and
2. Listing Page (http://lumalearn.net/tutorial/833/sql/sql-basics/sql-and-or-operator.html)
For Listing Page We need nice "Left Menu" at left side and Content Page (min 728px) at right side.
I need File PSD and/or Vector Only, without HTML code.

```html
<!DOCTYPE html>
<html lang="en">
<head>
<meta charset="utf-8">
<title>LumaLearn – SQL And / Or</title>
<link href="https://fonts.googleapis.com/css2?family=Oswald:wght@400;500&family=Open+Sans:wght@400;600;700&display=swap" rel="stylesheet">
<style>
:root{
  --ink:#222222;
  --dark:#262626;
  --darker:#1b1b1b;
  --page:#ececec;
  --card:#ffffff;
  --text:#444444;
  --muted:#7a7a7a;
  --line:#e2e2e2;
  --row:#f1f1f1;
  --row-alt:#f9f9f9;
  --blue:#1a73c9;
  --accent-yellow:#f2b500;
  --accent-red:#e8423c;
  --accent-green:#57b33e;
  --tag:#dcdcdc;
}
*{box-sizing:border-box;margin:0;padding:0}
html,body{width:1200px;height:2975px;overflow:hidden}
body{background:var(--page);font-family:"Open Sans",Arial,sans-serif;color:var(--text);position:relative}

/* header */
.site-header{position:absolute;left:0;top:0;width:1200px;height:93px;background:var(--dark)}
.brand{position:absolute;left:109px;top:28px;display:flex;align-items:center;gap:12px}
.brand-mark{width:34px;height:34px;background:var(--accent-yellow)}
.brand-name{font-family:"Oswald",sans-serif;font-size:30px;font-weight:400;color:#fff;line-height:1}
.main-nav{position:absolute;left:333px;top:30px;display:flex}
.main-nav a{font-family:"Oswald",sans-serif;font-size:16px;color:#fff;text-decoration:none;padding:4px 10px;line-height:24px}
.main-nav a.active{background:var(--blue)}
.header-search{position:absolute;left:815px;top:27px;display:flex}
.header-search .field{width:230px;height:40px;background:#fff;font-size:12px;color:#999;padding:12px 10px}
.header-search .go{width:44px;height:40px;background:var(--accent-yellow);display:flex;align-items:center;justify-content:center}

/* toolbar */
.toolbar{position:absolute;left:109px;top:113px;width:980px;height:32px}
.back-pill{position:absolute;left:0;top:0;width:151px;height:32px;background:var(--tag);border-radius:3px;display:flex;align-items:center;gap:12px;padding-left:8px;font-size:13px;color:var(--ink)}
.back-pill .dot{width:22px;height:22px;border-radius:50%;background:var(--ink);display:flex;align-items:center;justify-content:center}
.share-counts{position:absolute;left:403px;top:4px;display:flex;gap:6px}
.share-counts .btn{height:22px;border:1px solid #c9c9c9;background:#f6f6f6;font-size:11px;padding:0 6px;display:flex;align-items:center;color:#3a5a98;font-weight:700}
.share-counts .count{height:22px;border:1px solid #c9c9c9;background:#fff;font-size:11px;padding:0 6px;display:flex;align-items:center}
.alert-pill{position:absolute;left:577px;top:0;width:187px;height:32px;background:var(--tag);border-radius:3px;display:flex;align-items:center;gap:10px;padding-left:8px;font-size:13px;color:var(--ink)}
.tool-icons{position:absolute;right:0;top:0;display:flex;gap:10px}
.tool-icons span{width:32px;height:32px;background:var(--tag);border-radius:3px;display:flex;align-items:center;justify-content:center}

/* sidebar */
.side-menu{position:absolute;left:109px;top:165px;width:242px;height:2304px;background:var(--card);padding:16px 14px 0 16px}
.menu-group{margin-bottom:22px}
.menu-title{font-family:"Oswald",sans-serif;font-size:16px;color:var(--ink);background:var(--tag);height:31px;line-height:31px;padding-left:8px;margin-bottom:12px}
.menu-title.dark{background:var(--ink);color:#fff}
.menu-group li{list-style:none;height:30px;line-height:30px;border-bottom:1px solid #ececec;font-size:13px;color:#666;white-space:nowrap;overflow:hidden}
.menu-group li.current{color:var(--ink);font-weight:700}

/* content */
.card{position:absolute;left:373px;width:716px;background:var(--card);padding:0 20px}
.card-one{top:165px;height:1021px}
.card-two{top:1214px;height:872px}
.page-title{display:flex;justify-content:space-between;align-items:center;height:48px;margin-top:10px;border-bottom:2px solid var(--line)}
.page-title h1{font-family:"Oswald",sans-serif;font-weight:400;font-size:24px;color:var(--ink)}
.title-tools{display:flex;gap:12px;align-items:center}
.intro p{font-size:13px;color:var(--muted);margin-top:22px;line-height:18px}
.intro p:first-child{margin-top:26px}
.intro b{color:var(--blue)}
h2{font-family:"Oswald",sans-serif;font-weight:400;font-size:22px;color:var(--ink);line-height:30px}
.lead{font-size:13px;color:var(--muted);line-height:22px}
.data{width:676px;border-collapse:collapse;font-size:12px;color:var(--ink);table-layout:fixed}
.data th{background:var(--darker);color:#fff;font-weight:600;height:34px;text-align:left;padding-left:8px;font-size:12px}
.data td{height:30px;padding-left:8px;border-bottom:1px solid #fff;border-right:1px solid #fff;background:var(--row);white-space:nowrap;overflow:hidden}
.data tr:nth-child(even) td{background:var(--row-alt)}
.code-block{background:var(--tag);padding:10px 12px 14px}
.code-block pre{background:#fff;font-family:"Open Sans",Arial,sans-serif;font-size:12px;line-height:19px;color:var(--ink);padding:8px 10px}
.try-btn{display:inline-block;margin-top:8px;background:var(--blue);color:#fff;font-family:"Oswald",sans-serif;font-size:15px;width:133px;height:32px;line-height:32px;text-align:center}

/* ads */
.ad{position:absolute;top:2136px;height:282px}
.ad-one{left:385px;width:282px;background:linear-gradient(180deg,#1e5fa8 0%,#1b4f8c 35%,#f2f2f2 35%,#e6e6e6 100%)}
.ad-two{left:740px;width:335px;background:linear-gradient(135deg,#f4f6f8 0%,#e4e9ee 55%,#5a6470 100%)}

/* footer */
.stripe{position:absolute;left:0;top:2493px;width:1200px;height:5px;display:flex}
.stripe i{flex:1}
.site-footer{position:absolute;left:0;top:2498px;width:1200px;height:417px;background:var(--dark)}
.app-btn{position:absolute;left:125px;top:40px;width:244px;height:40px;background:var(--accent-red);color:#fff;font-family:"Oswald",sans-serif;font-size:15px;text-align:center;line-height:40px}
.social{position:absolute;left:387px;top:40px;display:flex;gap:8px}
.social span{width:36px;height:36px;border-radius:50%}
.foot-search{position:absolute;left:765px;top:40px;display:flex}
.foot-search .field{width:270px;height:40px;background:#fff;font-size:12px;color:#999;padding:12px 10px}
.foot-search .go{width:44px;height:40px;background:var(--accent-yellow);display:flex;align-items:center;justify-content:center}
.foot-cols{position:absolute;left:113px;top:124px;display:flex}
.foot-col{width:200px}
.foot-col:nth-child(2){width:203px}
.foot-col:nth-child(3){width:206px}
.foot-col:nth-child(4){width:196px}
.foot-col h3{font-family:"Oswald",sans-serif;font-weight:400;font-size:17px;color:#fff;padding-bottom:6px;border-bottom:2px solid #555;width:168px;margin-bottom:10px}
.foot-col li{list-style:none;font-size:11.5px;color:#bdbdbd;line-height:22px;white-space:nowrap}
.bottom-bar{position:absolute;left:0;top:2915px;width:1200px;height:60px;background:var(--darker);font-size:11.5px;color:#ccc}
.bottom-bar .copy{position:absolute;left:113px;top:22px}
.bottom-bar .links{position:absolute;right:111px;top:22px;display:flex}
.bottom-bar .links span{padding:0 8px;border-left:1px solid #555}
.bottom-bar .links span:first-child{border-left:0}
</style>
</head>
<body>

<header class="site-header">
  <div class="brand"><span class="brand-mark"></span><span class="brand-name">LumaLearn</span></div>
  <nav class="main-nav">
    <a href="#">HOME</a><a href="#">HTML</a><a href="#">CSS</a><a href="#">JAVASCRIPT</a><a href="#">PHP</a><a href="#" class="active">SQL</a><a href="#">JQUERY</a><a href="#">JSON</a>
  </nav>
  <div class="header-search">
    <div class="field">Search by Site Engine...</div>
    <div class="go"><svg width="16" height="16" viewBox="0 0 16 16"><circle cx="6.5" cy="6.5" r="4.5" fill="none" stroke="#fff" stroke-width="2"/><line x1="10" y1="10" x2="14" y2="14" stroke="#fff" stroke-width="2"/></svg></div>
  </div>
</header>

<div class="toolbar">
  <div class="back-pill"><span class="dot"><svg width="10" height="10" viewBox="0 0 10 10"><path d="M7 1 L3 5 L7 9" fill="none" stroke="#fff" stroke-width="2"/></svg></span>Search results</div>
  <div class="share-counts">
    <span class="btn">Like</span><span class="count">2</span>
    <span class="btn">+1</span><span class="count">0</span>
  </div>
  <div class="alert-pill"><svg width="24" height="16" viewBox="0 0 24 16"><rect x="1" y="1" width="22" height="14" fill="#444"/><path d="M1 1 L12 9 L23 1" fill="none" stroke="#ddd" stroke-width="1.5"/></svg>Email me course alerts</div>
  <div class="tool-icons">
    <span><svg width="14" height="14" viewBox="0 0 14 14"><path d="M8 2 L13 7 L8 12 V9 C4 9 2 10 1 13 C1 8 3 5 8 5 Z" fill="#222"/></svg></span>
    <span><svg width="14" height="14" viewBox="0 0 14 14"><rect x="1" y="5" width="7" height="4" rx="2" fill="none" stroke="#222" stroke-width="1.6" transform="rotate(-45 4.5 7)"/><rect x="6" y="5" width="7" height="4" rx="2" fill="none" stroke="#222" stroke-width="1.6" transform="rotate(-45 9.5 7)"/></svg></span>
    <span><svg width="14" height="14" viewBox="0 0 14 14"><rect x="3" y="1" width="8" height="4" fill="#222"/><rect x="1" y="5" width="12" height="5" fill="#222"/><rect x="3" y="9" width="8" height="4" fill="#fff" stroke="#222"/></svg></span>
  </div>
</div>

<aside class="side-menu">
  <div class="menu-group">
    <div class="menu-title dark">SQL TUTORIAL</div>
    <ul><li class="current">SQL Introduction</li><li>SQL Introduction</li><li>SQL Syntax</li><li>SQL Data Types (TableDesk)</li><li>SQL Data Type (PortaDB)</li><li>SQL Data Types (OrionBase)</li><li>SQL Data Types (Vertex Server)</li><li>SQL Reference</li><li>SQL Terminology</li></ul>
  </div>
  <div class="menu-group">
    <div class="menu-title">SQL BASICS</div>
    <ul><li>SQL And / Or</li><li>SQL Delete</li><li>SQL Distinct</li><li>SQL Group By</li><li>SQL Insert</li><li>SQL Not</li><li>SQL Order By</li><li>SQL Select</li><li>SQL Update</li><li>SQL Where</li><li>SQL Create Database</li><li>SQL Create Table</li><li>SQL Drop</li><li>SQL TRUNCATE</li></ul>
  </div>
  <div class="menu-group">
    <div class="menu-title">SQL ADVANCED</div>
    <ul><li>SQL Alias</li><li>SQL Alter</li><li>SQL Auto-increment</li><li>SQL Between</li><li>SQL Create Index</li><li>SQL In</li><li>SQL Isnull()</li><li>SQL Like</li><li>SQL Null Values</li><li>SQL Select Into</li><li>SQL Union</li><li>SQL Top</li><li>SQL View</li><li>SQL Wildcards</li></ul>
  </div>
  <div class="menu-group">
    <div class="menu-title">SQL CONSTRAINTS</div>
    <ul><li>SQL Constraints Overview</li><li>SQL Check</li><li>SQL Default</li><li>SQL Not Null</li><li>SQL Primary Key</li><li>SQL Foreign Key</li><li>SQL Unique</li></ul>
  </div>
  <div class="menu-group">
    <div class="menu-title">SQL JOINS</div>
    <ul><li>SQL Joins Overview</li><li>SQL Full</li><li>SQL Inner Join</li><li>SQL Left Join</li><li>SQL Right Join</li></ul>
  </div>
  <div class="menu-group">
    <div class="menu-title">SQL FUNCTIONS</div>
    <ul><li>SQL Functions Overview</li><li>SQL AVG ()</li><li>SQL COUNT()</li><li>SQL FIRST()</li><li>SQL FORMAT()</li><li>SQL LAST()</li><li>SQL LCASE() / LOWER()</li><li>SQL LEN()</li><li>SQL MAX()</li><li>SQL MID()</li><li>SQL MIN()</li><li>SQL NOW()</li><li>SQL ROUND()</li><li>SQL SUM()</li><li>SQL UCASE() / UPPER()</li></ul>
  </div>
</aside>

<main>
  <section class="card card-one">
    <div class="page-title">
      <h1>SQL And / Or</h1>
      <div class="title-tools">
        <svg width="20" height="16" viewBox="0 0 20 16"><path d="M8 1 L1 8 L8 15 V10 C13 10 16 11 19 15 C18 9 15 5 8 5 Z" fill="var(--blue)"/></svg>
        <svg width="18" height="16" viewBox="0 0 18 16"><path d="M3 6 V3 H14 V1 L17 4 L14 7 V5 H5 V6 Z M15 10 V13 H4 V15 L1 12 L4 9 V11 H13 V10 Z" fill="#999"/></svg>
        <svg width="16" height="16" viewBox="0 0 16 16"><path d="M8 1 L10 6 L15 6 L11 9.5 L12.5 15 L8 11.8 L3.5 15 L5 9.5 L1 6 L6 6 Z" fill="#aaa"/></svg>
      </div>
    </div>
    <div class="intro">
      <p>The AND &amp; OR operators are used to filter records based on more than one condition.</p>
      <p>The AND operator displays a record if <b>both</b> the first condition and the second condition is true.</p>
      <p>The OR operator displays a record if <b>either</b> the first condition or the second condition is true.</p>
    </div>

    <h2 style="margin-top:38px">Example with AND Operator</h2>
    <p class="lead" style="margin-bottom:10px">Consider the following "Buyers" table:</p>
    <table class="data">
      <colgroup><col style="width:84px"><col style="width:133px"><col style="width:159px"><col style="width:135px"><col style="width:93px"><col style="width:72px"></colgroup>
      <tr><th>Buyer ID</th><th>Buyer Name</th><th>Buyer Address</th><th>City</th><th>Country</th><th>Deposit</th></tr>
      <tr><td>1</td><td>David Clinton</td><td>Blue Lake 123</td><td>New York</td><td>USA</td><td>435.45</td></tr>
      <tr><td>2</td><td>Shea Roxanne</td><td>Santa Rose 123</td><td>Liverpool</td><td>England</td><td>234.12</td></tr>
      <tr><td>3</td><td>Bryan de Lima</td><td>Corcovado Street</td><td>Rio de Janeiro</td><td>Brazil</td><td>534.22</td></tr>
      <tr><td>4</td><td>Tjen Chun Yen</td><td>Zhonghua Street 456</td><td>Shanghai</td><td>China</td><td>234.12</td></tr>
      <tr><td>5</td><td>Sheila White</td><td>Santa San Marine 456</td><td>New York</td><td>USA</td><td>234.12</td></tr>
      <tr><td>6</td><td>Bryan Clinton</td><td>Blue Lake 123</td><td>Sidney</td><td>Australia</td><td>534.22</td></tr>
      <tr><td>7</td><td>David Clinton</td><td>Blue Lake 123</td><td>Sidney</td><td>Australia</td><td>4361.87</td></tr>
      <tr><td>8</td><td>Tjen Chun Yen</td><td>Blue Lake 123</td><td>Singapore City</td><td>Singapore</td><td>308.33</td></tr>
      <tr><td>9</td><td>Sheila White</td><td>Santa San Marine 456</td><td>Sidney</td><td>Australia</td><td>435.45</td></tr>
    </table>
    <p class="lead" style="margin-top:12px;line-height:18px">In this example, select only the "Buyers" with the BuyerName equal to "David Clinton" AND the Country equal to "Australia":</p>

    <h2 style="margin-top:36px;margin-bottom:10px">Example</h2>
    <div class="code-block">
      <pre>SELECT * FROM Buyers
WHERE BuyerName='David Clinton'
AND Country='Australia'</pre>
      <span class="try-btn">Try It Now</span>
    </div>
    <p class="lead" style="margin-top:30px;margin-bottom:8px">The Following is the result of the above example:</p>
    <table class="data">
      <colgroup><col style="width:84px"><col style="width:133px"><col style="width:159px"><col style="width:135px"><col style="width:93px"><col style="width:72px"></colgroup>
      <tr><th>Buyer ID</th><th>Buyer Name</th><th>Buyer Address</th><th>City</th><th>Country</th><th>Deposit</th></tr>
      <tr><td>7</td><td>David Clinton</td><td>Blue Lake 123</td><td>Sidney</td><td>Australia</td><td>4361.87</td></tr>
    </table>
  </section>

  <section class="card card-two">
    <h2 style="margin-top:14px">Example with OR Operator</h2>
    <p class="lead" style="line-height:18px;margin-bottom:14px">In this example, select only the Buyers with the BuyerName equal to "Tjen Chun Yen" OR the BuyerName equal to "Sheila White":</p>
    <div class="code-block">
      <pre>SELECT * FROM Buyers
WHERE BuyerName='Tjen Chun Yen' OR BuyerName='Sheila White'</pre>
      <span class="try-btn">Try It Now</span>
    </div>
    <p class="lead" style="margin-top:30px;margin-bottom:8px">The Following is the result of the above example:</p>
    <table class="data">
      <colgroup><col style="width:84px"><col style="width:133px"><col style="width:159px"><col style="width:135px"><col style="width:93px"><col style="width:72px"></colgroup>
      <tr><th>Buyer ID</th><th>Buyer Name</th><th>Buyer Address</th><th>City</th><th>Country</th><th>Deposit</th></tr>
      <tr><td>4</td><td>Tjen Chun Yen</td><td>Zhonghua Street 456</td><td>Shanghai</td><td>China</td><td>234.12</td></tr>
      <tr><td>5</td><td>Sheila White</td><td>Santa San Marine 456</td><td>New York</td><td>USA</td><td>234.12</td></tr>
      <tr><td>8</td><td>Tjen Chun Yen</td><td>Blue Lake 123</td><td>Singapore City</td><td>Singapore</td><td>308.33</td></tr>
      <tr><td>9</td><td>Sheila White</td><td>Santa San Marine 456</td><td>Sidney</td><td>Australia</td><td>435.45</td></tr>
    </table>

    <h2 style="margin-top:34px">Example with AND &amp; OR Operator</h2>
    <p class="lead" style="line-height:18px;margin-bottom:14px">In this example, select only the Buyers with the Country equal to "China" OR the Country equal to "Singapore" and BuyerName equal to "Tjen Chun Yen":</p>
    <div class="code-block">
      <pre>SELECT * FROM Buyers
WHERE (Country='China' OR Country='Singapore') AND BuyerName='Tjen Chun Yen'</pre>
      <span class="try-btn">Try It Now</span>
    </div>
    <p class="lead" style="margin-top:30px;margin-bottom:8px">The Following is the result of the above example:</p>
    <table class="data">
      <colgroup><col style="width:84px"><col style="width:133px"><col style="width:159px"><col style="width:135px"><col style="width:93px"><col style="width:72px"></colgroup>
      <tr><th>Buyer ID</th><th>Buyer Name</th><th>Buyer Address</th><th>City</th><th>Country</th><th>Deposit</th></tr>
      <tr><td>4</td><td>Tjen Chun Yen</td><td>Zhonghua Street 456</td><td>Shanghai</td><td>China</td><td>234.12</td></tr>
      <tr><td>8</td><td>Tjen Chun Yen</td><td>Blue Lake 123</td><td>Singapore City</td><td>Singapore</td><td>308.33</td></tr>
    </table>
  </section>

  <div class="ad ad-one" role="img" aria-label="Banner advertisement for a laptop computer with price and shop button"></div>
  <div class="ad ad-two" role="img" aria-label="Banner advertisement for a data analytics product with a demo button"></div>
</main>

<div class="stripe"><i style="background:var(--blue)"></i><i style="background:var(--accent-green)"></i><i style="background:var(--accent-yellow)"></i><i style="background:var(--accent-red)"></i></div>
<footer class="site-footer">
  <div class="app-btn">Free Download in MOBILE APP</div>
  <div class="social"><span style="background:#3b5998"></span><span style="background:#3aa9e0"></span><span style="background:#dd4b39"></span><span style="background:#e62117"></span><span style="background:#f26522"></span></div>
  <div class="foot-search">
    <div class="field">Search by Site Engine...</div>
    <div class="go"><svg width="16" height="16" viewBox="0 0 16 16"><circle cx="6.5" cy="6.5" r="4.5" fill="none" stroke="#fff" stroke-width="2"/><line x1="10" y1="10" x2="14" y2="14" stroke="#fff" stroke-width="2"/></svg></div>
  </div>
  <div class="foot-cols">
    <div class="foot-col"><h3>RANDOM HTML5</h3><ul><li>nav in html5</li><li>embed html5</li><li>Table Overview in html5</li><li>Geolocation</li><li>dl html5</li><li>html in html5</li><li>HTTP Status Messages in H...</li><li>Caption tag in html</li><li>var tag in html5</li><li>em tag in html5</li></ul></div>
    <div class="foot-col"><h3>RANDOM CANVAS</h3><ul><li>Canvas Semicircles</li><li>Canvas Line Cap</li><li>Canvas Pattern</li><li>Canvas Custom Paths</li><li>html5-canvas-rounded-corn...</li><li>Canvas Introduction</li><li>Canvas Image Loader</li><li>Canvas Circles</li><li>Canvas Custom Arc</li><li>Canvas Draw Images</li></ul></div>
    <div class="foot-col"><h3>RANDOM JAVASCRIPT</h3><ul><li>Javascript Looping</li><li>JS Math sin(x)</li><li>JS DOM Area Object</li><li>JS DOM Input Radio</li><li>JS Global undefined</li><li>JS String-HTML blink()</li><li>JS String-HTML anchor()</li><li>JS String Concat()</li><li>Javascript Array Concat()</li><li>Javascript Browser Window</li></ul></div>
    <div class="foot-col"><h3>RANDOM TRY IT</h3><ul><li>br tag example</li><li>table tag example</li><li>summary tag example</li><li>select tag example</li><li>body tag example</li><li>s tag example</li><li>canvas-draw-text-example...</li><li>nav tag example</li><li>u tag example</li><li>td tag example with rowsp...</li></ul></div>
    <div class="foot-col"><h3>RANDOM ARTICLES</h3><ul><li>How to Make SQL Syntax Hi...</li><li>How to Make Drop Down Men...</li><li>How to Make Sitemap.xml</li><li>How to get an input text ...</li><li>How to get of everything ...</li><li>How to make WHOIS lookups...</li><li>Create Transparency Anima...</li><li>How to Auto Select All Te...</li><li>Make A Lot of Circle Anim...</li><li>Changing text with innerh...</li></ul></div>
  </div>
</footer>
<div class="bottom-bar">
  <div class="copy">Copyright © 2015. LumaLearn , All rights reserved</div>
  <div class="links"><span>Tutorial</span><span>Articles</span><span>Try it</span><span>Canvas</span><span>Webtools</span><span>About</span><span>Terms</span><span>Privacy</span><span>Disclaime</span><span>Contact</span><span>FAQ</span></div>
</div>

</body>
</html>
```